Convert my PowerPoint mock up of a hiring process flow to simple, informative illustration with some

I need to create an illustration which is meant to be an overview of a hiring process for a medical training start up. I created a pretty rough PowerPoint mock up that hopefully shows what I am trying to do. My hope is that I would get the illustration created and can add it to my website. I have several other similar projects needed as well and probably ongoing graphic design work if we develop a good working relationship.

Site: www.brindlecare.com

Target Market(s)

Medical employers

Industry/Entity Type

Healthcare

Number of Pages Required

1 page

Font styles to use
Serif
Sans Serif

Colors
2fb6a2
85cae6

Requirements
Must have
• Simple illustration when done
Nice to have
• Fits very well with existing look and feel of site.
Should not have
• Not sure

```html
<!DOCTYPE html>
<html lang="en">
<head>
<meta charset="utf-8">
<title>BrindleCare Hiring Process</title>
<link href="https://fonts.googleapis.com/css2?family=Play:wght@400;700&family=Lato:wght@400;700&display=swap" rel="stylesheet">
<style>
:root{
  --teal:#2fb6a2;
  --teal-dark:#23917f;
  --sky:#85cae6;
  --ink:#2b2b2b;
  --white:#ffffff;
  --header:#eef0f4;
  --phone:#8a8a8a;
  --red:#f02d12;
  --footer:#cfe9f7;
  --stripe:#6cc0ec;
  --brand:#1d4f9c;
}
*{margin:0;padding:0;box-sizing:border-box}
html,body{width:1200px;height:849px;overflow:hidden}
body{position:relative;font-family:"Lato",sans-serif;color:var(--ink)}
.backdrop{position:absolute;inset:0;background:
  radial-gradient(ellipse at 20% 30%,#8fb4d8 0%,transparent 55%),
  radial-gradient(ellipse at 70% 25%,#b9a596 0%,transparent 50%),
  radial-gradient(ellipse at 90% 70%,#9c8e7e 0%,transparent 45%),
  radial-gradient(ellipse at 40% 95%,#86cff2 0%,transparent 50%),
  linear-gradient(180deg,#9fb0c6 0%,#8fa4b8 50%,#8ccbea 100%)}
.header{position:absolute;left:0;top:0;width:1200px;height:96px;background:var(--header);border-top:4px solid #8c93b8}
.brand{position:absolute;left:114px;top:30px;display:flex;align-items:center;gap:10px;font-family:"Play",sans-serif;font-weight:700;font-size:26px;color:var(--brand)}
.brand-dot{width:26px;height:26px;border-radius:50%;background:var(--brand)}
.phone{position:absolute;right:115px;top:36px;display:flex;align-items:center;gap:8px;font-family:"Play",sans-serif;font-size:21px;font-weight:700;color:var(--phone)}
.card{position:absolute;width:71px;height:84px;background:var(--white);text-align:center}
.card svg{margin-top:13px}
.card span{display:block;font-family:"Play",sans-serif;font-weight:700;font-size:14px;margin-top:3px}
.card.outline{border:1.5px solid var(--teal)}
.card.finalist{background:var(--sky);color:var(--white)}
.headline{position:absolute;left:111px;width:421px;text-align:center;font-family:"Play",sans-serif;font-weight:700;font-size:20px;line-height:27px;color:var(--white)}
.panel{position:absolute;background:var(--white)}
.badge{position:absolute;width:70px;height:70px;border-radius:50%;background:var(--teal);border:4px solid var(--white);display:flex;align-items:center;justify-content:center}
.lorem{position:absolute;left:111px;top:437px;width:421px;text-align:center;font-size:13.5px;line-height:21.5px}
.step{position:absolute;left:645px;width:445px;background:var(--white);display:flex;align-items:center}
.step .tile{width:64px;align-self:stretch;background:var(--teal);margin-left:13px;display:flex;align-items:center;justify-content:center}
.step p{margin-left:16px;font-family:"Play",sans-serif;font-weight:700;font-size:19.5px;line-height:25px}
.panel-title{position:absolute;left:645px;width:445px;top:366px;text-align:center;font-family:"Play",sans-serif;font-weight:700;font-size:20px}
.panel-note{position:absolute;left:668px;top:524px;font-family:"Play",sans-serif;font-size:15px}
.finalist-tag{position:absolute;left:997px;top:505px;width:71px;height:35px;background:var(--teal);border-radius:3px;color:var(--white);font-family:"Play",sans-serif;font-weight:700;font-size:14px;display:flex;align-items:center;justify-content:center;letter-spacing:.5px}
.start{position:absolute;left:780px;top:646px;width:162px;height:45px;background:var(--red);border:1px solid var(--white);color:var(--white);font-family:"Play",sans-serif;font-weight:700;font-size:19px;display:flex;align-items:center;justify-content:center;gap:7px}
.footer{position:absolute;left:0;top:793px;width:1200px;height:56px;background:var(--footer);border-bottom:6px solid var(--stripe);text-align:center;font-size:12.5px;font-weight:700;line-height:50px}
.lines{position:absolute;left:0;top:0}
</style>
</head>
<body>
<svg width="0" height="0" style="position:absolute">
  <defs>
    <symbol id="person" viewBox="0 0 36 36">
      <circle cx="18" cy="18" r="16.5" fill="none" stroke="currentColor" stroke-width="2"/>
      <circle cx="18" cy="14" r="6" fill="currentColor"/>
      <path d="M7 29c2-6 6-8 11-8s9 2 11 8a16 16 0 0 1-22 0z" fill="currentColor"/>
    </symbol>
    <symbol id="suit" viewBox="0 0 36 36">
      <circle cx="18" cy="11" r="7" fill="#fff"/>
      <path d="M4 34c1-9 6-13 14-13s13 4 14 13z" fill="#fff"/>
      <path d="M16 21h4l-1 3 1 8h-4l1-8z" fill="var(--teal)"/>
    </symbol>
  </defs>
</svg>

<div class="backdrop" role="img" aria-label="Softly blurred clinic interior in blue and warm beige tones"></div>

<header class="header">
  <div class="brand"><span class="brand-dot"></span>BrindleCare</div>
  <div class="phone">
    <svg width="22" height="22" viewBox="0 0 24 24"><circle cx="12" cy="12" r="10.5" fill="none" stroke="#555" stroke-width="1.6"/><path d="M8.5 7c.8-.6 1.5-.3 1.9.6l.6 1.3c.3.6 0 1.1-.5 1.4l-.5.3c.5 1.4 1.5 2.6 2.8 3.3l.4-.5c.4-.4 1-.5 1.5-.2l1.2.8c.8.5.9 1.3.2 1.9-1.4 1.2-3.5.7-5.4-1.1S7.1 8.4 8.5 7z" fill="#555"/></svg>
    0100-555-0142
  </div>
</header>

<svg class="lines" width="1200" height="849">
  <g stroke="#fff" stroke-width="1.2" fill="#fff">
    <path d="M148 633H510M148 633V668M235 633V668M324 633V668M413 633V668M510 633V668" fill="none"/>
    <circle cx="148" cy="668" r="3"/><circle cx="235" cy="668" r="3"/><circle cx="324" cy="668" r="3"/><circle cx="413" cy="668" r="3"/><circle cx="510" cy="668" r="3"/>
  </g>
  <g stroke="var(--teal)" stroke-width="1.2" fill="var(--teal)">
    <path d="M713 486V515M797 486V515M885 486V515M713 515H885" fill="none"/>
    <circle cx="713" cy="515" r="2.6"/><circle cx="797" cy="515" r="2.6"/><circle cx="885" cy="515" r="2.6"/>
  </g>
  <path d="M313 310L325 334L337 310L325 318Z" fill="rgba(255,255,255,.55)"/>
  <path d="M856 236L869 262L882 236L869 244Z" fill="rgba(255,255,255,.6)"/>
  <path d="M566 227L612 436L569 645L602 436Z" fill="#6d6d72" opacity=".85"/>
  <g fill="none" stroke="#dde3e6" stroke-width="2.2">
    <path d="M934 421l9 10-9 10M944 421l9 10-9 10M954 421l9 10-9 10"/>
    <path d="M934 455l9 10-9 10M944 455l9 10-9 10M954 455l9 10-9 10"/>
  </g>
</svg>

<!-- candidate pool -->
<div class="card" style="left:111px;top:134px;color:var(--sky)"><svg width="36" height="36"><use href="#person"/></svg><span style="color:var(--ink)">Resume</span></div>
<div class="card" style="left:198px;top:134px;color:var(--sky)"><svg width="36" height="36"><use href="#person"/></svg><span style="color:var(--ink)">Resume</span></div>
<div class="card" style="left:286px;top:134px;color:var(--sky)"><svg width="36" height="36"><use href="#person"/></svg><span style="color:var(--ink)">Resume</span></div>
<div class="card" style="left:373px;top:134px;color:var(--sky)"><svg width="36" height="36"><use href="#person"/></svg><span style="color:var(--ink)">Resume</span></div>
<div class="card" style="left:461px;top:134px;color:var(--sky)"><svg width="36" height="36"><use href="#person"/></svg><span style="color:var(--ink)">Resume</span></div>

<h2 class="headline" style="top:238px">Collect and Synthesize Candidates<br>for Training, Employment</h2>

<div class="panel" style="left:111px;top:388px;width:421px;height:155px"></div>
<div class="badge" style="left:286px;top:352px"><svg width="34" height="34"><use href="#suit"/></svg></div>
<p class="lorem">Lorem ipsum dolor sit amet, consectetuer adipiscin elit, sedml diam nonummy nibh euismod tincidunt ut laoreet dolore magna aliquam erat volutpat Lorem ipsum dolor sit amet, consectetuer Lorem ipsum dolor sit amet, consectetuer.</p>

<h2 class="headline" style="top:559px">Employer Selects Their Favored<br>Candidates To Interview</h2>

<div class="card" style="left:111px;top:681px;color:var(--sky)"><svg width="36" height="36"><use href="#person"/></svg><span style="color:var(--ink)">Resume</span></div>
<div class="card" style="left:198px;top:681px;color:var(--sky)"><svg width="36" height="36"><use href="#person"/></svg><span style="color:var(--ink)">Resume</span></div>
<div class="card" style="left:286px;top:681px;color:var(--sky)"><svg width="36" height="36"><use href="#person"/></svg><span style="color:var(--ink)">Resume</span></div>
<div class="card" style="left:373px;top:681px;color:var(--sky)"><svg width="36" height="36"><use href="#person"/></svg><span style="color:var(--ink)">Resume</span></div>
<div class="card" style="left:461px;top:681px;color:var(--sky)"><svg width="36" height="36"><use href="#person"/></svg><span style="color:var(--ink)">Resume</span></div>

<!-- right flow -->
<div class="step" style="top:134px;height:84px">
  <div class="tile"><svg width="44" height="40" viewBox="0 0 44 40" fill="#fff"><rect x="18" y="3" width="22" height="14" fill="none" stroke="#fff" stroke-width="2"/><circle cx="11" cy="8" r="4"/><path d="M5 22c0-5 3-8 6-8l8-2v3l-5 3v4z"/><circle cx="8" cy="28" r="3"/><circle cx="18" cy="28" r="3"/><circle cx="28" cy="28" r="3"/><circle cx="38" cy="28" r="3"/><path d="M3 38c0-4 2-6 5-6s5 2 5 6zM13 38c0-4 2-6 5-6s5 2 5 6zM23 38c0-4 2-6 5-6s5 2 5 6zM33 38c0-4 2-6 5-6s5 2 5 6z"/></svg></div>
  <p>Employer,BrindleCare Agree Upon<br>Training Protocol</p>
</div>

<div class="panel" style="left:645px;top:317px;width:445px;height:249px"></div>
<div class="badge" style="left:832px;top:281px"><svg width="34" height="34"><use href="#suit"/></svg></div>
<h3 class="panel-title">Candidates Interviewed By Employer</h3>
<div class="card outline" style="left:673px;top:402px;color:var(--sky)"><svg width="36" height="36"><use href="#person"/></svg><span style="color:var(--ink)">Resume</span></div>
<div class="card outline" style="left:760px;top:402px;color:var(--sky)"><svg width="36" height="36"><use href="#person"/></svg><span style="color:var(--ink)">Resume</span></div>
<div class="card outline" style="left:848px;top:402px;color:var(--sky)"><svg width="36" height="36"><use href="#person"/></svg><span style="color:var(--ink)">Resume</span></div>
<div class="card finalist" style="left:998px;top:402px;color:var(--white)"><svg width="36" height="36"><use href="#person"/></svg><span>Resume</span></div>
<div class="finalist-tag">FINALIST</div>
<p class="panel-note">Candidates Interviewed By Employer</p>

<div class="step" style="top:579px;height:49px">
  <div class="tile"><svg width="32" height="30" viewBox="0 0 32 30" fill="none" stroke="#fff" stroke-width="2"><circle cx="10" cy="8" r="5"/><path d="M2 26c0-7 4-10 8-10s6 2 7 4"/><rect x="16" y="18" width="14" height="9"/><circle cx="22" cy="12" r="3"/></svg></div>
  <p>BrindleCare Pre-Employment Training</p>
</div>

<div class="start">
  <svg width="22" height="20" viewBox="0 0 22 20" fill="#fff"><rect x="0" y="8" width="5" height="12"/><path d="M7 8l5-7c1.5-1 3 0 2.6 1.8L13.5 7H20c1.2 0 2 1 1.8 2.2l-1.6 8.6c-.2 1.2-1 2.2-2.2 2.2H7z"/></svg>
  START JOB!
</div>

<div class="step" style="top:716px;height:48px">
  <div class="tile"><svg width="28" height="30" viewBox="0 0 28 30" fill="#fff"><circle cx="14" cy="10" r="6"/><path d="M6 11a8 8 0 0 1 16 0" fill="none" stroke="#fff" stroke-width="2"/><path d="M3 30c0-7 5-11 11-11s11 4 11 11z"/></svg></div>
  <p>Post Employment Support (1-3 months)</p>
</div>

<footer class="footer">Copyright©&nbsp; 2015 Brindle Care. All Rights Reserved.</footer>
</body>
</html>
```